VelliFilez Website

VelliFiles - Orderly Medical Filez
We need a Web design for a new company called - VelliFilez.
VelliFilez is a Personal Injury and Medical Record Legal Service Outsourcing company. We help Personal Injury Attorneys - with fact based Medical Chronologies and Summaries.

We take Medical Records in disarray and put them in order and summarize them in a chronological order and Update them as needed (if more medical records are added)
Take Releases (for medical records) and work with doctor practices and get the records if needed

Target Market(s)

Personal Injury Attorneys

Industry/Entity Type

Attorney

Number of Pages Required

2 page

Font styles to use
Serif
Sans Serif

Colors

Designer to choose colors to be used in the design.

Requirements
Must have
• Professional Design
• Just need the design for the Home page and Internal pages - I will do the Coding for the pages in html and/or wordpress.
• Don't worry about the content - just need a design.

```html
<!DOCTYPE html>
<html lang="en">
<head>
<meta charset="utf-8">
<title>VelliFilez – Home</title>
<link href="https://fonts.googleapis.com/css2?family=Nunito:wght@400;600&family=Open+Sans:wght@400;600&family=Roboto+Condensed:wght@400;700&display=swap" rel="stylesheet">
<style>
:root{
  --navy:#0d2366;
  --royal:#1f3f9c;
  --pill:#2a4cb8;
  --ink:#1d1d1d;
  --body:#555;
  --muted:#6b6b6b;
  --band:#ebebeb;
  --footer:#0b0b0b;
  --white:#fff;
}
*{margin:0;padding:0;box-sizing:border-box}
html,body{width:1200px;height:3061px;overflow:hidden}
body{position:relative;background:var(--white);font-family:"Open Sans",sans-serif;color:var(--body)}
.abs{position:absolute}

/* Hero */
.hero{left:0;top:0;width:1200px;height:690px;
  background:linear-gradient(100deg,#8a7a64 0%,#b9ac98 30%,#9b8f80 52%,#3d3f4a 70%,#6a6660 85%,#c9c2b8 100%)}
.hero-shade{left:0;top:0;width:1200px;height:690px;background:linear-gradient(180deg,rgba(0,0,0,.25),rgba(0,0,0,0) 40%)}
.logo{left:98px;top:38px;color:var(--white);text-align:center}
.logo-mark{display:block;width:30px;height:30px;border:3px solid var(--white);margin:0 auto 6px}
.logo-name{font-family:"Nunito",sans-serif;font-size:30px;font-weight:600;letter-spacing:2px;line-height:1}
.logo-tag{font-size:10px;letter-spacing:1.5px;margin-top:4px}
.nav{right:80px;top:56px;display:flex;gap:6px}
.nav a{color:var(--white);text-decoration:none;font-size:19px;padding:9px 22px;border-radius:22px}
.nav a.active{background:var(--pill)}
.hero-title{left:92px;top:240px;color:var(--white);font-family:"Roboto Condensed",sans-serif}
.hero-title h1{font-size:62px;font-weight:700;letter-spacing:1px;line-height:1}
.hero-title p{font-size:25px;line-height:37px;margin-top:16px}
.hero-arrows{left:92px;top:410px;display:flex;gap:10px}

/* Welcome */
.welcome{left:88px;top:518px;width:1024px;height:258px;background:var(--navy);color:var(--white);text-align:center;padding:40px 56px}
.welcome h2{font-family:"Nunito",sans-serif;font-weight:400;font-size:34px;margin-bottom:18px}
.welcome p{font-size:15.5px;line-height:27px}

/* Services */
.section-title{width:1200px;left:0;text-align:center;font-family:"Nunito",sans-serif;font-weight:400;font-size:36px;color:var(--ink)}
.service{top:978px;width:300px;text-align:center}
.service .ring{width:106px;height:106px;border:2px solid var(--navy);border-radius:50%;margin:0 auto;display:flex;align-items:center;justify-content:center}
.service h3{font-family:"Nunito",sans-serif;font-weight:400;font-size:24px;color:var(--ink);margin-top:20px}
.service p{font-size:13.5px;line-height:24px;margin-top:10px;color:var(--muted);padding:0 14px}
.link{font-size:13.5px;color:var(--navy);text-decoration:none;display:inline-block;margin-top:4px}

/* What we do */
.band{left:0;top:1300px}
.wwd-back{left:114px;top:1470px;width:316px;height:318px;background:var(--royal)}
.wwd-photo{left:138px;top:1495px;width:308px;height:325px;background:linear-gradient(150deg,#8c7a66,#d8dde4 45%,#a4b4c8 75%,#6c6458);box-shadow:0 10px 22px rgba(0,0,0,.35)}
.wwd-text{left:486px;top:1508px;width:540px}
.wwd-text h2{font-family:"Nunito",sans-serif;font-weight:400;font-size:34px;color:var(--ink);margin-bottom:16px}
.wwd-text p{font-size:15.5px;line-height:28px;text-align:justify}
.btn{display:inline-block;background:var(--navy);color:var(--white);font-size:13.5px;padding:9px 18px;border-radius:18px;margin-top:22px;text-decoration:none}

/* News */
.card{top:2112px;width:313px}
.card-photo{width:313px;height:174px;position:relative}
.date{position:absolute;left:0;bottom:0;display:flex;font-size:12px;color:var(--white)}
.date span{padding:3px 10px}
.date .d{background:var(--royal)}
.date .c{background:#222}
.card h3{font-family:"Open Sans",sans-serif;font-weight:400;font-size:16.5px;color:var(--ink);margin-top:20px}
.card p{font-size:12.5px;line-height:19px;color:var(--muted);margin-top:10px}
.card .link{font-size:12.5px;margin-top:10px}

/* Partners */
.partner{top:2510px;width:172px;height:102px;background:#efefef;border:1px solid #ddd;border-radius:4px;box-shadow:0 2px 4px rgba(0,0,0,.08)}
.partner i{display:block;width:90px;height:16px;background:#cfcfcf;border-radius:3px;margin:43px auto 0}

/* Footer */
.footer{left:0;top:2667px;width:1200px;height:394px;background:var(--footer);color:var(--white)}
.newsletter{left:280px;top:50px;display:flex;align-items:center}
.newsletter h4{font-family:"Nunito",sans-serif;font-weight:400;font-size:27px;letter-spacing:1px;margin-right:30px}
.nl-input{width:346px;height:44px;background:var(--white);border-radius:22px 0 0 22px;color:#999;font-size:12px;padding:14px 18px}
.nl-btn{height:44px;background:var(--navy);border-radius:0 22px 22px 0;font-size:13px;padding:13px 16px}
.divider{left:97px;top:138px;width:1006px;height:1px;background:#2a2a2a}
.fcol{top:172px;font-size:12.5px;line-height:23px}
.fcol h5{font-weight:400;font-size:15px;margin-bottom:10px}
.fcol li{list-style:none}
.fcol li::before{content:"» ";}
.social{display:flex;gap:12px;margin-top:8px}
.social i{width:28px;height:28px;border-radius:50%;background:var(--white);display:block}
.copy{left:0;top:356px;width:1200px;text-align:center;font-size:12px}
</style>
</head>
<body>

<header>
  <div class="abs hero" role="img" aria-label="Photo of a bearded man in glasses and suit working at a desk in an office with bookshelves"></div>
  <div class="abs hero-shade"></div>
  <div class="abs logo">
    <span class="logo-mark"></span>
    <div class="logo-name">VELLIFILEZ</div>
    <div class="logo-tag">Orderly Medical Filez</div>
  </div>
  <nav class="abs nav">
    <a class="active" href="#">Home</a><a href="#">About us</a><a href="#">Services</a><a href="#">Projects</a><a href="#">Blog</a><a href="#">Contact us</a>
  </nav>
  <div class="abs hero-title">
    <h1>VELLIFILEZ</h1>
    <p>A Personal Injury and Medical Record<br>Legal Service Outsourcing company</p>
  </div>
  <div class="abs hero-arrows">
    <svg width="20" height="20" viewBox="0 0 20 20"><path d="M13 4 7 10l6 6" fill="none" stroke="#fff" stroke-width="2.5"/></svg>
    <svg width="20" height="20" viewBox="0 0 20 20"><path d="M7 4l6 6-6 6" fill="none" stroke="#fff" stroke-width="2.5"/></svg>
  </div>
</header>

<section class="abs welcome">
  <h2>Welcome to VelliFilez</h2>
  <p>It is a long established fact that a reader will be distracted by the readable content of a page when looking at its layout. The point of using Lorem Ipsum is that it has a more-or-less normal distribution of letters, as opposed to using 'Content here, content here', making it look like readable English. Many desktop publishing packages and web page editors now use Lorem Ipsum as their default model text, and a search for 'lorem ipsum' will uncover many web sites still in their infancy.</p>
</section>

<section>
  <h2 class="abs section-title" style="top:880px">Our Services</h2>
  <div class="abs service" style="left:126px">
    <div class="ring"><svg width="50" height="56" viewBox="0 0 50 56"><circle cx="25" cy="14" r="10" fill="#0d2366"/><path d="M5 54c0-14 8-24 20-24s20 10 20 24z" fill="#0d2366"/><rect x="21" y="34" width="8" height="14" fill="#fff"/></svg></div>
    <h3>Personal Injury</h3>
    <p>It is a long established fact that a reader will be distracted by the readable</p>
    <a class="link" href="#">Learn More -&gt;</a>
  </div>
  <div class="abs service" style="left:448px">
    <div class="ring"><svg width="40" height="52" viewBox="0 0 40 52"><path d="M2 2h26l10 10v38H2z" fill="#0d2366"/><path d="M8 28h6l3-6 4 12 3-6h8" fill="none" stroke="#fff" stroke-width="2"/><path d="M8 40h24M8 45h18" stroke="#fff" stroke-width="2"/></svg></div>
    <h3>Medical Record</h3>
    <p>It is a long established fact that a reader will be distracted by the readable</p>
    <a class="link" href="#">Learn More -&gt;</a>
  </div>
  <div class="abs service" style="left:768px">
    <div class="ring"><svg width="44" height="52" viewBox="0 0 44 52"><rect x="2" y="6" width="32" height="44" rx="3" fill="#0d2366"/><rect x="11" y="2" width="14" height="8" rx="2" fill="#0d2366" stroke="#fff" stroke-width="1.5"/><path d="M8 20h18M8 28h14M8 36h10" stroke="#fff" stroke-width="2"/><path d="M40 18 24 40l-4 4 1-6 16-22z" fill="#0d2366" stroke="#fff" stroke-width="1.5"/></svg></div>
    <h3>Summaries</h3>
    <p>It is a long established fact that a reader will be distracted by the readable content</p>
    <a class="link" href="#">Learn More -&gt;</a>
  </div>
</section>

<section>
  <svg class="abs band" width="1200" height="630" viewBox="0 0 1200 630"><polygon points="0,102 1200,10 1200,628 0,628" fill="#ebebeb"/></svg>
  <div class="abs wwd-back"></div>
  <div class="abs wwd-photo" role="img" aria-label="Photo of hands filling in a medical record form"></div>
  <div class="abs wwd-text">
    <h2>What We Do</h2>
    <p>It is a long established fact that a reader will be distracted by the readable content of a page when looking at its layout. The point of using Lorem Ipsum is that it has a more-or-less normal distribution of letters, as opposed to using 'Content here, content here', making it look like readable English. Many desktop publishing packages and web page editors now use Lorem Ipsum as their default model text, and a search for 'lorem ipsum' will uncover many web sites still in their infancy.</p>
    <a class="btn" href="#">Read More »</a>
  </div>
</section>

<section>
  <h2 class="abs section-title" style="top:2024px">Latest News</h2>
  <article class="abs card" style="left:92px">
    <div class="card-photo" role="img" aria-label="Photo of a person reviewing charts on paper at a desk" style="background:linear-gradient(120deg,#c68a4e,#e9d2b4 50%,#8e6b4e)">
      <div class="date"><span class="d">Dec 03</span><span class="c">0</span></div>
    </div>
    <h3>Porro quisquam est qui dolorem</h3>
    <p>It has survived not only five centuries, but also the leap into electronic typesetting,</p>
    <a class="link" href="#">Read More »</a>
  </article>
  <article class="abs card" style="left:440px">
    <div class="card-photo" role="img" aria-label="Photo of a doctor writing on a medical form with a blue pen" style="background:linear-gradient(120deg,#6f8bb3,#e6ebf1 45%,#c8b28e)">
      <div class="date"><span class="d">Dec 03</span><span class="c">0</span></div>
    </div>
    <h3>Neque porro quisquam est dolorem</h3>
    <p>It has survived not only five centuries, but also the leap into electronic typesetting,</p>
    <a class="link" href="#">Read More »</a>
  </article>
  <article class="abs card" style="left:793px">
    <div class="card-photo" role="img" aria-label="Photo of hands sorting paper documents" style="background:linear-gradient(120deg,#232a3a,#c9c4b6 55%,#2d3444)">
      <div class="date"><span class="d">Dec 03</span><span class="c">0</span></div>
    </div>
    <h3>Dolorem ipsum quia dolor sit amet,</h3>
    <p>It has survived not only five centuries, but also the leap into electronic typesetting,</p>
    <a class="link" href="#">Read More »</a>
  </article>
</section>

<section aria-label="Partners">
  <div class="abs partner" style="left:148px"><i></i></div>
  <div class="abs partner" style="left:331px"><i></i></div>
  <div class="abs partner" style="left:515px"><i></i></div>
  <div class="abs partner" style="left:698px"><i></i></div>
  <div class="abs partner" style="left:881px"><i></i></div>
</section>

<footer class="abs footer">
  <div class="abs newsletter">
    <h4>NEWSLETTER</h4>
    <div class="nl-input">email@example.com</div>
    <div class="nl-btn">SUBSCRIBE</div>
  </div>
  <div class="abs divider"></div>
  <div class="abs fcol" style="left:97px">
    <h5>INFORMATION</h5>
    <ul><li>Privacy Policy</li><li>Your Account</li><li>Advanced Search</li><li>Contact Us</li></ul>
  </div>
  <div class="abs fcol" style="left:372px">
    <h5>LINKS</h5>
    <ul><li>Home</li><li>Research</li><li>About us</li><li>Services</li></ul>
  </div>
  <div class="abs fcol" style="left:615px">
    <h5>CONTACT US</h5>
    <p>Address : Lindelaan 12B 3012 KM<br>Rotterdam Nederland</p>
    <p>Phone : +31 (0)10-555 0199</p>
    <p>Email : info@vellifilez.example</p>
  </div>
  <div class="abs fcol" style="left:938px">
    <h5>FOLLOW US OUT THERE</h5>
    <div class="social"><i></i><i></i><i></i></div>
  </div>
  <div class="abs copy">Copyright © 2018. All Rights Reserved</div>
</footer>

</body>
</html>
```